Brightleaf Notes

We need two websites: both are already online, using Drupal.
I would prefer to use Drupal for both, so if you know nothing about Drupal, or wld prefer to use Wordpress please don't submit a proposal.
One website will be a blog. The domain is brightleafnotes.com.
For this site, we need to be able to post blogs; take comments; invite members; perhaps send out a weekly newsletter; and perhaps introduce weekly interactive elements e.g. a poll.
The other website is to house a new company. The domain is tkmpower.com.
This would also be very simple, allowing for administrator and third party posts and blogs, and interactive elements such as forums.
Neither project is ambitious; the priority is a simple to use, attractive, professional looking shop window.
Updates

i havent had much interest in this web design and coding project; am therefore happy to make brief the project easier/ better value - i need coding, and that is included in the fee. but am happy to limit this to home page for one website; we can negotiate a higher fee for an additional home page for another website; and i am happy if you work in wordpress or other; i prefer drupal simply because that is the template we are using at present. in addition i am happy to guarantee the project for the right designer, if thats a priority

Reason: project extended just to give us time to make a decision on Monday/ Tuesday !

Industry/Entity Type

Online

Coding

Coded - Design and coding required

```html
<!DOCTYPE html>
<html lang="en">
<head>
<meta charset="utf-8">
<title>Brightleaf Notes</title>
<link href="https://fonts.googleapis.com/css2?family=Arimo:wght@400;700&display=swap" rel="stylesheet">
<style>
:root{
  --orange:#e8661a;
  --blue:#2a9fd6;
  --ink:#222;
  --text:#5a5a5a;
  --muted:#8a8a8a;
  --line:#e6e6e6;
  --panel:#fff;
  --panel-soft:#f7f7f7;
  --footer:#2d2a2e;
}
*{box-sizing:border-box;margin:0;padding:0}
html,body{width:1200px;height:3082px;overflow:hidden}
body{position:relative;font-family:"Arimo",Arial,sans-serif;color:var(--text);background:#5a3d6e}
.backdrop{position:absolute;inset:0;background:linear-gradient(180deg,#a8bfae 0%,#7fa7a3 10%,#3f7f8a 25%,#4a7b86 38%,#6b5a7e 50%,#5a3d6e 65%,#4b2f5c 82%,#3a2549 100%)}
.site-header{position:absolute;left:0;top:0;width:1200px;height:82px;background:var(--panel);box-shadow:0 2px 6px rgba(0,0,0,.2);z-index:2}
.brand{position:absolute;left:117px;top:18px;display:flex;align-items:center;gap:10px}
.brand-dot{width:26px;height:26px;border-radius:50%;background:var(--orange)}
.brand-name{font-size:18px;font-weight:400;color:var(--blue)}
.brand-tagline{position:absolute;left:153px;top:46px;font-size:11px;font-style:italic;color:var(--blue)}
.main-nav{position:absolute;top:31px;left:0;width:100%;font-size:16px}
.main-nav a{position:absolute;color:var(--muted);text-decoration:none}
.main-nav a.active{color:var(--blue)}
.post{position:absolute;left:117px;width:654px;height:658px;background:var(--panel)}
.post-image{position:absolute;left:0;top:0;width:654px;height:378px}
.author-photo{position:absolute;left:29px;top:331px;width:100px;height:100px;border:3px solid #fff;background:linear-gradient(135deg,#c9c9c9,#6d6d6d)}
.author-name{position:absolute;left:150px;top:341px;color:#fff;font-size:15px}
.post-meta{position:absolute;left:150px;top:420px;font-size:12px;color:#444;display:flex;align-items:center;gap:6px}
.post-meta svg{width:13px;height:13px}
.post-title{position:absolute;left:26px;top:455px;font-size:24px;font-weight:400;color:var(--ink)}
.post-excerpt{position:absolute;left:26px;top:492px;width:600px;font-size:14.5px;line-height:25.5px;color:#555}
.post-footer{position:absolute;left:0;top:600px;width:100%;height:58px;border-top:1px solid var(--line);background:var(--panel-soft)}
.read-more{position:absolute;left:26px;top:15px;width:100px;height:32px;border-radius:4px;background:var(--orange);color:#fff;font-size:11px;line-height:32px;text-align:center}
.share{position:absolute;right:26px;top:17px;display:flex;gap:4px}
.share span{width:24px;height:24px;border:1px solid #d8d8d8;background:#fff}
.widget{position:absolute;left:797px;width:286px;background:var(--panel);padding:18px 18px}
.widget-title{font-size:13px;color:var(--ink);padding-bottom:8px;position:relative}
.widget-title::after{content:"";position:absolute;left:0;bottom:0;width:110px;height:2px;background:var(--orange)}
.search-box{margin-top:20px;height:30px;border:1px solid var(--orange);display:flex}
.search-box span{flex:1;font-size:11px;font-style:italic;color:var(--orange);padding:8px}
.search-box i{width:28px;background:var(--orange);display:flex;align-items:center;justify-content:center}
.post-list{list-style:none;margin-top:22px}
.post-list li{display:flex;gap:10px;height:88px}
.thumb{width:68px;height:68px;flex:none}
.post-list h4{font-size:13px;font-weight:700;color:var(--orange);margin-bottom:4px}
.post-list p{font-size:11px;line-height:17px;color:var(--muted)}
.follow-list{list-style:none;margin-top:22px}
.follow-list li{display:flex;height:37px;margin-bottom:6px}
.follow-list i{width:37px;height:37px;flex:none}
.follow-list span{flex:1;background:#f1f1f1;font-size:11px;color:var(--muted);line-height:37px;padding-left:20px}
.newsletter p{margin-top:20px;font-size:10.5px;line-height:20px;color:#555}
.email-field{margin-top:16px;height:30px;border:1px solid #ddd;font-size:11px;color:#555;padding:8px 12px;display:flex;gap:10px;align-items:center}
.signup{margin-top:16px;width:60px;height:24px;border-radius:3px;background:var(--orange);color:#fff;font-size:11px;text-align:center;line-height:24px}
.pagination{position:absolute;left:117px;top:2953px;display:flex;gap:11px}
.pagination span{width:32px;height:32px;background:#fff;text-align:center;line-height:32px;font-size:13px;color:var(--orange)}
.pagination span.current{color:var(--ink)}
.site-footer{position:absolute;left:0;top:3022px;width:1200px;height:60px;background:var(--footer);border-top:4px solid var(--orange);font-size:11px;color:#bbb}
.footer-nav{position:absolute;left:117px;top:22px}
.footer-nav a{color:#bbb;text-decoration:none}
.footer-nav a:first-child{color:var(--orange)}
.copyright{position:absolute;right:117px;top:18px}
</style>
</head>
<body>
<div class="backdrop" role="img" aria-label="Full-page photograph of a sea horizon over a purple-toned rocky shore"></div>

<header class="site-header">
  <div class="brand"><span class="brand-dot"></span><span class="brand-name">Brightleaf Notes</span></div>
  <div class="brand-tagline">Intelligent comment, from Martin Hale and Simon Voss</div>
  <nav class="main-nav">
    <a class="active" href="#" style="left:713px">Home</a>
    <a href="#" style="left:801px">About Us</a>
    <a href="#" style="left:918px">Blog</a>
    <a href="#" style="left:998px">Contact us</a>
  </nav>
</header>

<article class="post" style="top:123px">
  <div class="post-image" role="img" aria-label="Photo of a child holding autumn leaves" style="background:linear-gradient(135deg,#c9892e,#8a5a1e 60%,#3d4a6a)"></div>
  <div class="author-photo" role="img" aria-label="Author portrait"></div>
  <div class="author-name">Martin Hale</div>
  <div class="post-meta"><svg viewBox="0 0 14 14"><circle cx="7" cy="7" r="6" fill="none" stroke="#444" stroke-width="1.5"/><path d="M7 3.5V7l2.5 1.5" fill="none" stroke="#444" stroke-width="1.5"/></svg>Thursday, July 03, 2014 &nbsp;/ <svg viewBox="0 0 14 14"><path d="M1 2h9v6H5l-3 3V8H1z" fill="#444"/></svg>4 Comments</div>
  <h2 class="post-title">Paradox of European power prices…</h2>
  <p class="post-excerpt">Power prices is not an easy topic to talk about. First and foremost, there are lots of different power prices from baseload to peak, from wholesale to retail, from heavy industry to commercial prices. And each country across...</p>
  <div class="post-footer"><span class="read-more">Read More</span><div class="share"><span></span><span></span><span></span><span></span><span></span><span></span></div></div>
</article>

<article class="post" style="top:828px">
  <div class="post-image" role="img" aria-label="Photo of a worker sitting on solar panels under a blue sky" style="background:linear-gradient(180deg,#6fa3d8,#cfe0ef 30%,#3a4f7a 55%,#2b3656)"></div>
  <div class="author-photo" role="img" aria-label="Author portrait"></div>
  <div class="author-name">Martin Hale</div>
  <div class="post-meta"><svg viewBox="0 0 14 14"><circle cx="7" cy="7" r="6" fill="none" stroke="#444" stroke-width="1.5"/><path d="M7 3.5V7l2.5 1.5" fill="none" stroke="#444" stroke-width="1.5"/></svg>Thursday, July 03, 2014 &nbsp;/ <svg viewBox="0 0 14 14"><path d="M1 2h9v6H5l-3 3V8H1z" fill="#444"/></svg>4 Comments</div>
  <h2 class="post-title">Paradox of European power prices…</h2>
  <p class="post-excerpt">Power prices is not an easy topic to talk about. First and foremost, there are lots of different power prices from baseload to peak, from wholesale to retail, from heavy industry to commercial prices. And each country across...</p>
  <div class="post-footer"><span class="read-more">Read More</span><div class="share"><span></span><span></span><span></span><span></span><span></span><span></span></div></div>
</article>

<article class="post" style="top:1531px">
  <div class="post-image" role="img" aria-label="Photo of a businesswoman with a sunflower and a piggy bank in front of solar panels" style="background:linear-gradient(160deg,#8fb4d6,#d9e4ee 35%,#4a6a94 65%,#2c3a58)"></div>
  <div class="author-photo" role="img" aria-label="Author portrait"></div>
  <div class="author-name">Martin Hale</div>
  <div class="post-meta"><svg viewBox="0 0 14 14"><circle cx="7" cy="7" r="6" fill="none" stroke="#444" stroke-width="1.5"/><path d="M7 3.5V7l2.5 1.5" fill="none" stroke="#444" stroke-width="1.5"/></svg>Thursday, July 03, 2014 &nbsp;/ <svg viewBox="0 0 14 14"><path d="M1 2h9v6H5l-3 3V8H1z" fill="#444"/></svg>4 Comments</div>
  <h2 class="post-title">Paradox of European power prices…</h2>
  <p class="post-excerpt">Power prices is not an easy topic to talk about. First and foremost, there are lots of different power prices from baseload to peak, from wholesale to retail, from heavy industry to commercial prices. And each country across...</p>
  <div class="post-footer"><span class="read-more">Read More</span><div class="share"><span></span><span></span><span></span><span></span><span></span><span></span></div></div>
</article>

<article class="post" style="top:2236px">
  <div class="post-image" role="img" aria-label="Photo of two children fishing by a pond" style="background:linear-gradient(180deg,#4f7a2e,#7a9a45 40%,#3d5a2a 60%,#1f2e20)"></div>
  <div class="author-photo" role="img" aria-label="Author portrait"></div>
  <div class="author-name">Martin Hale</div>
  <div class="post-meta"><svg viewBox="0 0 14 14"><circle cx="7" cy="7" r="6" fill="none" stroke="#444" stroke-width="1.5"/><path d="M7 3.5V7l2.5 1.5" fill="none" stroke="#444" stroke-width="1.5"/></svg>Thursday, July 03, 2014 &nbsp;/ <svg viewBox="0 0 14 14"><path d="M1 2h9v6H5l-3 3V8H1z" fill="#444"/></svg>4 Comments</div>
  <h2 class="post-title">Paradox of European power prices…</h2>
  <p class="post-excerpt">Power prices is not an easy topic to talk about. First and foremost, there are lots of different power prices from baseload to peak, from wholesale to retail, from heavy industry to commercial prices. And each country across...</p>
  <div class="post-footer"><span class="read-more">Read More</span><div class="share"><span></span><span></span><span></span><span></span><span></span><span></span></div></div>
</article>

<aside>
  <section class="widget" style="top:123px;height:117px">
    <h3 class="widget-title" style="font-weight:400">Search This Blog</h3>
    <div class="search-box"><span>Search...</span><i><svg width="14" height="14" viewBox="0 0 14 14"><circle cx="6" cy="6" r="4" fill="none" stroke="#fff" stroke-width="2"/><path d="M9 9l4 4" stroke="#fff" stroke-width="2"/></svg></i></div>
  </section>

  <section class="widget" style="top:265px;height:327px">
    <h3 class="widget-title" style="font-weight:400">Popular Post</h3>
    <ul class="post-list">
      <li><div class="thumb" role="img" aria-label="Post thumbnail photo" style="background:linear-gradient(135deg,#6a9ac4,#3f6a3a)"></div><div><h4>Duis vitae orci ac nequeu</h4><p>Lorem ipsum dolor sit ametns adipiscing eli ente sque situ...</p></div></li>
      <li><div class="thumb" role="img" aria-label="Post thumbnail photo" style="background:linear-gradient(135deg,#6d6d6d,#2e2e2e)"></div><div><h4>Duis vitae orci ac nequeu</h4><p>Lorem ipsum dolor sit ametnet adipiscing elit. Pellente situ...</p></div></li>
      <li><div class="thumb" role="img" aria-label="Post thumbnail photo" style="background:linear-gradient(135deg,#c98a5e,#7a4a2e)"></div><div><h4>Duis vitae orci ac nequlla</h4><p>Lorem ipsum dolor sit conset adipiscing elit. Pellentesqu...</p></div></li>
    </ul>
  </section>

  <section class="widget" style="top:608px;height:327px">
    <h3 class="widget-title" style="font-weight:400">Recent Post</h3>
    <ul class="post-list">
      <li><div class="thumb" role="img" aria-label="Post thumbnail photo" style="background:linear-gradient(135deg,#6a9ac4,#3f6a3a)"></div><div><h4>Duis vitae orci ac nequeu</h4><p>Lorem ipsum dolor sit ametns adipiscing eli ente sque situ...</p></div></li>
      <li><div class="thumb" role="img" aria-label="Post thumbnail photo" style="background:linear-gradient(135deg,#6d6d6d,#2e2e2e)"></div><div><h4>Duis vitae orci ac nequeu</h4><p>Lorem ipsum dolor sit ametnet adipiscing elit. Pellente situ...</p></div></li>
      <li><div class="thumb" role="img" aria-label="Post thumbnail photo" style="background:linear-gradient(135deg,#c98a5e,#7a4a2e)"></div><div><h4>Duis vitae orci ac nequlla</h4><p>Lorem ipsum dolor sit conset adipiscing elit. Pellentesqu...</p></div></li>
    </ul>
  </section>

  <section class="widget" style="top:964px;height:335px">
    <h3 class="widget-title" style="font-weight:400">Follow us</h3>
    <ul class="follow-list">
      <li><i style="background:#2aa9e0"></i><span>133 Followers</span></li>
      <li><i style="background:#3b5998"></i><span>3449 Likes</span></li>
      <li><i style="background:#d9302b"></i><span>1943 Subcribes</span></li>
      <li><i style="background:#d6492f"></i><span>3449 followers</span></li>
      <li><i style="background:#cb2027"></i><span>16533 Followers</span></li>
      <li><i style="background:#4e7fa3"></i><span>78594 followers</span></li>
    </ul>
  </section>

  <section class="widget newsletter" style="top:1327px;height:210px">
    <h3 class="widget-title" style="font-weight:400">Weekly Newletters</h3>
    <p>Complete the form below,and we'll send you<br>And get our latest article deliver to your inbox</p>
    <div class="email-field"><svg width="14" height="10" viewBox="0 0 14 10"><rect x=".5" y=".5" width="13" height="9" fill="none" stroke="#999"/><path d="M.5.5L7 6l6.5-5.5" fill="none" stroke="#999"/></svg>mail@brightleafnotes.com</div>
    <div class="signup">Sign up</div>
  </section>
</aside>

<nav class="pagination"><span class="current">1</span><span>2</span><span>3</span><span>»</span></nav>

<footer class="site-footer">
  <div class="footer-nav"><a href="#">Home</a> / <a href="#">About Us</a> / <a href="#">Blog</a> / <a href="#">Contact us</a></div>
  <div class="copyright">2014 Brightleaf Notes,All rights reaved</div>
</footer>
</body>
</html>
```